" Venda através de catálogo, indicação e mídias sociais , sem loja fisica. Produto será entregue em caixas personalizadas para consumo e presentear. "

```html
<!DOCTYPE html>
<html lang="pt-BR">
<head>
<meta charset="utf-8">
<title>Sucrée – Brigadeiros &amp; Doces Gourmet</title>
<link rel="stylesheet" href="https://fonts.googleapis.com/css2?family=Playfair+Display:wght@500&family=Montserrat:wght@500&display=swap">
<style>
  :root {
    --cocoa: #3e2b22;
    --cocoa-band: #4a342a;
    --cocoa-deep: #2f2019;
    --gold: #d9b36a;
    --gold-light: #f0d79a;
    --gold-dark: #a8823f;
  }
  html, body {
    margin: 0;
    padding: 0;
    width: 1200px;
    height: 1200px;
    overflow: hidden;
    background: var(--cocoa);
  }
  .canvas {
    position: relative;
    width: 1200px;
    height: 1200px;
    background: var(--cocoa);
  }
  .banner {
    position: absolute;
    left: 0;
    top: 372px;
    width: 1200px;
    height: 456px;
  }
  .brand {
    position: absolute;
    left: 735px;
    top: 435px;
    width: 330px;
    height: 330px;
    display: flex;
    flex-direction: column;
    align-items: center;
    justify-content: center;
    text-align: center;
  }
  .brand-name {
    font-family: "Playfair Display", serif;
    font-weight: 500;
    font-size: 72px;
    line-height: 1;
    color: var(--gold);
    margin: 0;
  }
  .brand-tagline {
    font-family: "Montserrat", sans-serif;
    font-weight: 500;
    font-size: 17px;
    letter-spacing: 0.5px;
    color: var(--gold-light);
    margin: 14px 0 0;
  }
</style>
</head>
<body>
<main class="canvas">
  <svg class="banner" viewBox="0 0 1200 456" xmlns="http://www.w3.org/2000/svg">
    <defs>
      <linearGradient id="cupcake-tones" x1="0" y1="0" x2="1" y2="1">
        <stop offset="0" stop-color="#e9ddd2"/>
        <stop offset="0.5" stop-color="#b98f78"/>
        <stop offset="1" stop-color="#5a3426"/>
      </linearGradient>
      <linearGradient id="cakepop-tones" x1="0" y1="0" x2="1" y2="1">
        <stop offset="0" stop-color="#cfc6c0"/>
        <stop offset="0.5" stop-color="#6b4b3d"/>
        <stop offset="1" stop-color="#d8d2cd"/>
      </linearGradient>
      <linearGradient id="gold-ribbon" x1="0" y1="0" x2="1" y2="0">
        <stop offset="0" stop-color="var(--gold-dark)"/>
        <stop offset="0.5" stop-color="var(--gold-light)"/>
        <stop offset="1" stop-color="var(--gold-dark)"/>
      </linearGradient>
    </defs>

    <rect class="band-fill" x="0" y="0" width="1200" height="456" fill="var(--cocoa-band)"
          role="img" aria-label="Padrão losangular sutil em marrom chocolate"/>

    <polygon class="photo-cupcakes" points="0,0 444,0 228,456 0,456" fill="url(#cupcake-tones)"
             role="img" aria-label="Foto de cupcakes de chocolate com cobertura de creme"/>
    <polygon class="photo-cakepops" points="468,0 720,0 504,456 252,456" fill="url(#cakepop-tones)"
             role="img" aria-label="Foto de cake pops de chocolate com confeitos dourados"/>

    <g class="gold-rules" stroke="var(--gold)" stroke-width="5" fill="none">
      <line x1="110" y1="0" x2="0" y2="232"/>
      <line x1="444" y1="0" x2="228" y2="456"/>
      <line x1="468" y1="0" x2="252" y2="456"/>
      <line x1="720" y1="0" x2="504" y2="456"/>
    </g>

    <rect class="gold-ribbon" x="864" y="0" width="60" height="456" fill="url(#gold-ribbon)"/>
    <circle class="brand-disc" cx="894" cy="228" r="165" fill="var(--cocoa-deep)"/>
  </svg>

  <div class="brand">
    <p class="brand-name">Sucrée</p>
    <p class="brand-tagline">Brigadeiros &amp; Doces Gourmet</p>
  </div>
</main>
</body>
</html>
```